Occupational Therapist does home accessibility for disabled folks; needs business card design

We need a business card for a company in Portland, Oregon that specializes in making homes accessible, comfortable, and functional for people who are disabled or aging who would like to stay in THEIR home. Our medical background as Occupational Therapists allows us to translate the functional needs of the person into the recommendations for the design of the home remodel.

Target Market(s)

Elderly, children of elderly
People with disabilities, families of people with disabilities

Industry/Entity Type

Business

Contact Information for Business Card

Company name: Nestabode
Name: Karen Dwyer Lopez, OTR/L, CAPS, ECHM
Occupational Therapist, Home Modification & Accessibility Specialist
website: www.homewellsteady.com
email: homewellsteady@mailbright.com
phone: (503)418-2957
CCB #: 384517

Font styles to use
Sans Serif

Requirements
Must have
• My logo
• Easy to read font with contrasting background
• Please list the Services offered: Occupational Therapy, Home safety & accessibility assessments, Home modification consulting, project management
Nice to have
• Friendly, welcoming feel
Should not have
• Dark colored background

```html
<!DOCTYPE html>
<html lang="en">
<head>
<meta charset="utf-8">
<title>Nestabode Business Card</title>
<link rel="stylesheet" href="https://fonts.googleapis.com/css2?family=Source+Sans+3:wght@400;600;700&display=swap">
<style>
  :root {
    --backdrop: #ebe7e2;
    --kraft-light: #cdab78;
    --kraft-mid: #c09b66;
    --kraft-dark: #b38d59;
    --ink: #1b1712;
  }
  * { box-sizing: border-box; margin: 0; padding: 0; }
  html, body {
    width: 1200px;
    height: 900px;
    overflow: hidden;
  }
  body {
    position: relative;
    background: var(--backdrop);
    font-family: "Source Sans 3", "Myriad Pro", Arial, sans-serif;
    color: var(--ink);
  }
  .card {
    position: absolute;
    width: 556px;
    height: 342px;
    background: linear-gradient(135deg, var(--kraft-light) 0%, var(--kraft-mid) 55%, var(--kraft-dark) 100%);
    box-shadow: 0 6px 18px rgba(0, 0, 0, 0.18);
    text-align: center;
  }
  .card--front { left: 238px; top: 62px; }
  .card--back { left: 459px; top: 519px; }

  .holder-name {
    position: absolute;
    top: 51px; left: 0; right: 0;
    font-size: 20px;
    font-weight: 600;
  }
  .holder-title {
    position: absolute;
    top: 81px; left: 0; right: 0;
    font-size: 16.5px;
    line-height: 20px;
  }
  .license {
    position: absolute;
    top: 165px; left: 0; right: 0;
    font-size: 15px;
  }
  .license b { font-weight: 700; }
  .contact {
    position: absolute;
    top: 198px; left: 0; right: 0;
    font-size: 15px;
    line-height: 19.5px;
    list-style: none;
  }
  .tagline {
    position: absolute;
    top: 282px; left: 0; right: 0;
    font-size: 18.5px;
  }

  .brand {
    position: absolute;
    top: 88px; left: 0; right: 0;
    display: flex;
    align-items: center;
    justify-content: center;
    gap: 16px;
  }
  .brand-mark {
    width: 38px;
    height: 38px;
    background: var(--ink);
  }
  .brand-name {
    font-size: 58px;
    font-weight: 700;
    line-height: 1;
    color: var(--ink);
  }
  .services-heading {
    position: absolute;
    top: 216px; left: 0; right: 0;
    font-size: 19px;
    font-weight: 700;
  }
  .services {
    position: absolute;
    top: 255px; left: 0; right: 0;
    font-size: 16.5px;
    line-height: 20px;
  }
  .services span { white-space: nowrap; margin: 0 5px; }
  .services span::before { content: "\25CF"; font-size: 10px; margin-right: 6px; position: relative; top: -2px; }
</style>
</head>
<body>
  <section class="card card--front" aria-label="Card front">
    <h1 class="holder-name">Karen Dwyer Lopez,OTR/L, CAPS, ECHM</h1>
    <p class="holder-title">Occupational Therapist, Home Modification<br>&amp; Accessibility Specialist</p>
    <p class="license"><b>CCB #:</b> 384517</p>
    <ul class="contact">
      <li>(503)418-2957</li>
      <li>homewellsteady@mailbright.com</li>
      <li>www.homewellsteady.com</li>
    </ul>
    <p class="tagline">YOUR HOME, SHAPED AROUND YOU</p>
  </section>

  <section class="card card--back" aria-label="Card back">
    <div class="brand">
      <span class="brand-mark"></span>
      <span class="brand-name">Nestabode</span>
    </div>
    <h2 class="services-heading">Services offered</h2>
    <p class="services">
      <span>Occupational Therapy</span><span>Home Safety &amp; Accessibility Assessments,</span><br>
      <span>Home Modification Consulting</span><span>Project Management</span>
    </p>
  </section>
</body>
</html>
```